Preisliste für Tochterunternehmen im Baustoff-Sektor
Zielgruppe
Wir möchten für unserer Tochterunternehmen im Baustoff-Sektor eine gestaltete Preisliste.
Es gibt eine Liste für Privat- und Geschäftskunden die bisher mit MS-Office einfach gehalten war.
Aufgabenstellung
Logo und der aktuelle Briefkopf sind in der Anlage. Das Design sollte zum CI passen (siehe Briefkopf)
Vom Platzbedarf her sollte sich an der alten Liste orientiert werden. Weitere Infos und Bilder gibt es unter www.tannhoferwerk.de
Genaue Firmenbezeichnung usw. finden Sie in der Preisliste auf der letzten Seite

```html
<!DOCTYPE html>
<html lang="de">
<head>
<meta charset="utf-8">
<title>Preisliste Tannhofer Werk</title>
<link href="https://fonts.googleapis.com/css2?family=Source+Sans+3:wght@400;600;700;800&display=swap" rel="stylesheet">
<style>
  :root{
    --brand-dark:#7a7064;
    --brand-light:#aca79c;
    --row-a:#e8e6e3;
    --row-b:#e1dcd4;
    --ink:#1f1f1f;
    --logo:#77716a;
    --photo-1:#7b7565;
    --photo-2:#5a5a60;
    --photo-3:#7f8a5c;
    --photo-4:#6b6a55;
    --photo-5:#7a5f42;
  }
  *{margin:0;padding:0;box-sizing:border-box}
  html,body{width:1200px;height:1200px;overflow:hidden;background:#fff}
  body{position:relative;font-family:"Source Sans 3",sans-serif;color:var(--ink)}
  .page{position:absolute;top:146px;width:867px;height:1225px;background:#fff;overflow:hidden;
    transform:scale(.625);transform-origin:0 0;box-shadow:4px 4px 14px rgba(0,0,0,.22)}
  .page-left{left:40px}
  .page-right{left:620px}

  .brand{position:absolute;left:572px;top:40px;display:flex;align-items:center;gap:12px}
  .brand-mark{width:34px;height:34px;background:var(--logo)}
  .brand-name{font-weight:800;font-size:31px;line-height:27px;color:var(--logo);letter-spacing:.5px}

  .title{position:absolute;left:41px;top:123px;font-size:16.5px;line-height:22px}
  .title strong{font-weight:600}

  .contact{position:absolute;left:574px;top:122px;border-left:2px solid var(--brand-dark);padding-left:8px;font-size:13.5px;line-height:16.7px;white-space:nowrap}
  .contact strong{font-weight:700}
  .contact .ico{display:inline-block;width:13px;height:12px;vertical-align:-2px;margin-right:9px}

  .tbl-head{position:absolute;display:grid;gap:2px;height:34px;color:#fff;font-size:15px;font-weight:600;letter-spacing:.3px;white-space:nowrap}
  .tbl-head div{background:var(--brand-dark);padding:0 8px;display:flex;align-items:center}
  .tbl-head .n{justify-content:center}

  .row{position:absolute;display:grid;gap:2px;font-size:13.5px;line-height:16.6px}
  .row > div{padding:0 8px;display:flex;align-items:center;white-space:nowrap}
  .row > .num{justify-content:flex-end;text-align:right}
  .row > .top{display:block;padding-top:4px}
  .row > .num.top{text-align:right}
  .a > div{background:var(--row-a)}
  .b > div{background:var(--row-b)}

  .col-s{left:43px;width:590px;grid-template-columns:342px 121px 123px}
  .col-w{left:43px;width:783px;grid-template-columns:534px 121px 124px}
  .col-z{left:43px;width:590px;grid-template-columns:341px 121px 124px}

  .desc-sub{display:grid!important;grid-template-columns:1fr 133px;padding:4px 8px 0!important;align-items:start}

  .photo{position:absolute;left:656px;width:170px}
  .caption{position:absolute;left:656px;font-size:11px}
  .note{position:absolute;left:49px;top:690px;font-size:10.5px;white-space:nowrap}
  .fine{position:absolute;left:41px;top:1114px;width:774px;font-size:10.3px;line-height:13.6px}

  .foot-light{position:absolute;left:0;top:1184px;width:429px;height:41px;background:var(--brand-light)}
  .foot-dark{position:absolute;left:437px;top:1184px;width:430px;height:41px;background:var(--brand-dark);
    color:#fff;font-size:13px;font-weight:600;letter-spacing:.6px;display:flex;justify-content:center;padding-top:10px}
</style>
</head>
<body>

<section class="page page-left">
  <div class="brand"><span class="brand-mark"></span><div class="brand-name">TANNHOFER<br>WERK</div></div>
  <div class="title"><strong>Preisliste gültig ab 01.03.2018</strong><br>für Tannhofer Grauwacke aus unserem Werk Tannhof</div>
  <div class="contact">
    <strong>Konrad Wetzlinger Baustoff GmbH &amp; Co. KG</strong><br>
    Lindenhofer Str. 12<br>56299 Tannhof<br>
    <svg class="ico" viewBox="0 0 12 12"><path d="M2 1l2 0 1 3-1.5 1a7 7 0 0 0 3.5 3.5L8 7l3 1v2c0 1-1 1-1 1A9 9 0 0 1 1 2s0-1 1-1z" fill="#222"/></svg>04711-38-0<br>
    <svg class="ico" viewBox="0 0 12 12"><rect x="3" y="1" width="6" height="3" fill="#222"/><rect x="1" y="4" width="10" height="5" rx="1" fill="#222"/><rect x="3" y="7" width="6" height="4" fill="#fff" stroke="#222"/></svg>04711-38-500<br>
    <svg class="ico" viewBox="0 0 12 12"><rect x="1" y="2.5" width="10" height="7" fill="#222"/><path d="M1 2.5l5 4 5-4" stroke="#fff" fill="none"/></svg>info@tannhoferwerk.de<br>
    <svg class="ico" viewBox="0 0 12 12"><circle cx="6" cy="6" r="5.5" fill="#222"/><path d="M1 6h10M6 .5c-3 3-3 8 0 11M6 .5c3 3 3 8 0 11" stroke="#fff" stroke-width=".8" fill="none"/></svg>www.tannhoferwerk.de
  </div>

  <div class="tbl-head col-s" style="top:275px"><div>Schüttgut</div><div class="n">Netto ab Werk</div><div class="n">Brutto ab Werk</div></div>
  <div class="row col-s a" style="top:319px;height:23px"><div>Vorsiebmaterial*</div><div class="num">5,00 €/t</div><div class="num">5,95 €/t</div></div>
  <div class="row col-s a" style="top:343px;height:23px"><div>Mineralgemisch 0/32 ; 0/45*</div><div class="num">7,50 €/t</div><div class="num">8,93 €/t</div></div>
  <div class="row col-s a" style="top:367px;height:23px"><div>Steinmaterial gebrochen 0/100 ; 0/150 ; 0/200*</div><div class="num">6,50 €/t</div><div class="num">7,74 €/t</div></div>
  <div class="row col-s b" style="top:399px;height:23px"><div>Frostschutz-Splitt 0/32 ; 0/45</div><div class="num">9,00 €/t</div><div class="num">10,71 €/t</div></div>
  <div class="row col-s b" style="top:423px;height:23px"><div>Schottertragschicht 0/32 ; 0/45</div><div class="num">10,00 €/t</div><div class="num">11,90 €/t</div></div>
  <div class="row col-s a" style="top:454px;height:23px"><div>Brechsand 0/3; 0/4*</div><div class="num">8,00 €/t</div><div class="num">9,52 €/t</div></div>
  <div class="row col-s b" style="top:486px;height:23px"><div>Splitt 2/5; 2/8; 5/8; 8/16; 16/22; 16/32; 22/32; 32/56</div><div class="num">16,00 €/t</div><div class="num">19,04 €/t</div></div>
  <div class="row col-s a" style="top:517px;height:23px"><div>Splitt gewaschen 2/4; 4/8; 8/16; 16/22</div><div class="num">18,00 €/t</div><div class="num">21,42 €/t</div></div>
  <div class="row col-s b" style="top:548px;height:23px"><div>Splitt-Gemische 0/5 ; 0/8 ; 0/11 ; 0/16*</div><div class="num">13,00 €/t</div><div class="num">15,47 €/t</div></div>
  <div class="row col-s a" style="top:579px;height:23px"><div>Wingertsschotter 20/60*</div><div class="num">15,00 €/t</div><div class="num">17,85 €/t</div></div>
  <div class="row col-s a" style="top:603px;height:23px"><div>Schotter 40/80 ; 56/90*</div><div class="num">14,00 €/t</div><div class="num">16,66 €/t</div></div>
  <div class="row col-s a" style="top:627px;height:23px"><div>Schotter 70/100 ;&nbsp; 70/150* als Gabionen Füllmaterial</div><div class="num">20,00 €/t</div><div class="num">23,80 €/t</div></div>
  <div class="row col-s b" style="top:659px;height:23px"><div>Sackware 2/5; 8/16 (20 kg)</div><div class="num">5,00 €/St</div><div class="num">5,95 €/St</div></div>
  <div class="note">* nicht güteüberwacht &nbsp;/&nbsp; Schüttgüter-Kleinmengen bis 3 to werden pauschal mit 3 to abgerechnet</div>

  <div class="photo" role="img" aria-label="Foto Trockenmauerwerk mit Bepflanzung" style="top:275px;height:117px;background:linear-gradient(180deg,#5f6b4a,var(--photo-1) 45%,#6b5a48)"></div>
  <div class="caption" style="top:394px">Trockenmauerwerk</div>
  <div class="photo" role="img" aria-label="Foto Bruchsteinmauerwerk" style="top:423px;height:115px;background:linear-gradient(180deg,#4c4a48,var(--photo-2) 40%,#6e6658)"></div>
  <div class="caption" style="top:540px">Bruchsteinmauerwerk</div>
  <div class="photo" role="img" aria-label="Foto Mauer aus Schichtsteinen mit Hecke" style="top:567px;height:115px;background:linear-gradient(180deg,#6f8a4a,var(--photo-3) 45%,#777268 70%,#8a877e)"></div>
  <div class="caption" style="top:686px">Schichtsteine</div>

  <div class="tbl-head col-w" style="top:725px"><div>Handsortierte- und bearbeitete Materialien</div><div class="n">Netto ab Werk</div><div class="n">Brutto ab Werk</div></div>
  <div class="row col-w a" style="top:771px;height:55px"><div class="top">Mauersteine für <b>Trockenmauerwerk</b>, nach DIN 1053 Bild 14<br>Schichthöhe ca. 10-35 cm, Einbindetiefe ca. 15-40 cm, <b>unbearbeitet</b>, von Hand sortiert,<br>Gewicht ca. 2-70 kg/Stein Ergiebigkeit ca. 1,2-1,5 m²/t</div><div class="num">115,00 €/t</div><div class="num">136,85 €/t</div></div>
  <div class="row col-w b" style="top:833px;height:40px"><div class="top">Wie vor, jedoch Einbindetiefe ca. 10-30 cm, Schichthöhe von ca. 10-35 cm<br>Ergiebigkeit ca. 1,8-2,0 m²/t</div><div class="num">125,00 €/t</div><div class="num">148,75 €/t</div></div>
  <div class="row col-w a" style="top:882px;height:55px"><div class="top">Mauersteine für <b>Bruchsteinmauerwerk</b> nach DIN 1053 Bild 16<br>Schichthöhe ca. 10-35 cm, Einbindetiefe ca. 10-30 cm, <b>unbearbeitet</b>, von Hand sortiert,<br>Gewicht ca. 2-50 kg/Stein Ergiebigkeit ca. 2,0-2,4 m²/t</div><div class="num">125,00 €/t</div><div class="num">148,75 €/t</div></div>
  <div class="row col-w b" style="top:945px;height:40px"><div class="top">Wie vor, jedoch Einbindetiefe &lt; 15 cm, Schichthöhe von 8-25 cm<br>Ergiebigkeit ca. 3,5-4,0 m²/t</div><div class="num">240,00 €/t</div><div class="num">285,6 €/t</div></div>
  <div class="row col-w a" style="top:993px;height:55px"><div class="top"><b>Schichtsteine</b>, von Hand sortiert und masch. bearbeitet nach DIN 1053 Bild 17<br>Sichtfläche <b>spaltrauh</b>, Schichthöhe von 8-25 cm, Einbautiefe ca. 12-25 cm<br>Ergiebigkeit ca. 2,6-3,0 m²/t</div><div class="num">255,00 €/t</div><div class="num">303,45 €/t</div></div>
  <div class="row col-w b" style="top:1056px;height:40px"><div class="top">Wie vor, jeoch Einbindetiefe &lt; 15 cm, Schichthöhe von 4-15 cm<br>Ergiebigkeit ca. 4,0-4,5 m²/t</div><div class="num">310,00 €/t</div><div class="num">368,90 €/t</div></div>
  <div class="row col-w a" style="top:1104px;height:55px"><div class="top"><b>Schichtsteine</b>, von Hand bearbeitet und behauen nach DIN 1053 Bild 17<br>Sichtfläche <b>bossiert</b>, Schichthöhe 4-12 cm, 12-25 cm und 4-25 cm<br>Einbindetiefe ca. 8-25 cm</div><div class="num">150,00 €/m²</div><div class="num">178,50 €/m²</div></div>

  <div class="foot-light"></div>
  <div class="foot-dark">www.tannhoferwerk.de</div>
</section>

<section class="page page-right">
  <div class="brand"><span class="brand-mark"></span><div class="brand-name">TANNHOFER<br>WERK</div></div>
  <div class="title" style="top:125px"><strong>Preisliste gültig ab 01.03.2018</strong><br>für Tannhofer Grauwacke aus unserem Werk Tannhof</div>
  <div class="contact" style="top:123px">
    <strong>Konrad Wetzlinger Baustoff GmbH &amp; Co. KG</strong><br>
    Lindenhofer Str. 12<br>56299 Tannhof<br>
    <svg class="ico" viewBox="0 0 12 12"><path d="M2 1l2 0 1 3-1.5 1a7 7 0 0 0 3.5 3.5L8 7l3 1v2c0 1-1 1-1 1A9 9 0 0 1 1 2s0-1 1-1z" fill="#222"/></svg>04711-38-0<br>
    <svg class="ico" viewBox="0 0 12 12"><rect x="3" y="1" width="6" height="3" fill="#222"/><rect x="1" y="4" width="10" height="5" rx="1" fill="#222"/><rect x="3" y="7" width="6" height="4" fill="#fff" stroke="#222"/></svg>04711-38-500<br>
    <svg class="ico" viewBox="0 0 12 12"><rect x="1" y="2.5" width="10" height="7" fill="#222"/><path d="M1 2.5l5 4 5-4" stroke="#fff" fill="none"/></svg>info@tannhoferwerk.de<br>
    <svg class="ico" viewBox="0 0 12 12"><circle cx="6" cy="6" r="5.5" fill="#222"/><path d="M1 6h10M6 .5c-3 3-3 8 0 11M6 .5c3 3 3 8 0 11" stroke="#fff" stroke-width=".8" fill="none"/></svg>www.tannhoferwerk.de
  </div>

  <div class="tbl-head col-w" style="top:279px"><div>Handsortierte- und bearbeitete Materialien</div><div class="n">Netto ab Werk</div><div class="n">Brutto ab Werk</div></div>
  <div class="row col-w a" style="top:322px;height:41px"><div class="top"><b>Kräuterschnecke</b>, 1x Holzkiste mit handsortierten Mauersteinen,<br>1 Big Bag mit 500 kg Splitt 0/16, Aufbauanleitung</div><div class="num">350,00 €/St</div><div class="num">416,50 €/St</div></div>
  <div class="row col-w b" style="top:370px;height:40px"><div class="top"><b>Böschungspflaster</b> ca. 25-30 cm stark, unbearbeitet, von Hand sortiert,<br>Gewicht ca. 30-100 kg/Stein, Ergiebigkeit ca. 1,5 - 2,0 m²/t</div><div class="num">90,00 €/t</div><div class="num">107,10 €/t</div></div>
  <div class="row col-w a" style="top:418px;height:23px"><div><span><b>Findlingsmauersteine</b>, Kantenlänge ca. 30-60 / 60-100 / 100-140 cm, lagerhaft</span></div><div class="num">120,00 €/t</div><div class="num">142,80 €/t</div></div>
  <div class="row col-w b" style="top:449px;height:23px"><div><span><b>Findlingssteine</b>, polygonal / unregelmäßig</span></div><div class="num">90,00 €/t</div><div class="num">107,10 €/t</div></div>
  <div class="row col-w a" style="top:479px;height:41px"><div class="desc-sub"><span><b>Findling</b> Einzelstück, eckig oder rund</span><span>&lt; 1 t<br>&gt; 1 t</span></div><div class="num top">160,00 €/St<br>240,00 €/St</div><div class="num top">190,40 €/St<br>285,60 €/St</div></div>
  <div class="row col-w b" style="top:529px;height:74px"><div class="desc-sub"><span><b>Rollschicht</b>, von Hand bearbeitet (Höhe/Breite)</span><span>150/300 ; 100/400<br>150/400 ; 200/450<br>200/500 ; 250/500<br>200/550 ; 250/550</span></div><div class="num top">145,00 €/lfm<br>145,00 €/lfm<br>155,00 €/lfm<br>165,00 €/lfm</div><div class="num top">172,55 €/lfm<br>172,55 €/lfm<br>184,45 €/lfm<br>196,35 €/lfm</div></div>
  <div class="row col-w a" style="top:612px;height:23px"><div><span><b>Bogensteine</b>, von Hand bearbeitet, bis 20 cm hoch</span></div><div class="num">120,00 €/lfm</div><div class="num">142,80 €/lfm</div></div>
  <div class="row col-w b" style="top:643px;height:23px"><div><span><b>Ecksteine</b>, von Hand bearbeitet</span></div><div class="num">95,00 €/lfm</div><div class="num">113,05 €/lfm</div></div>
  <div class="row col-w a" style="top:674px;height:23px"><div><span><b>Platten</b>, unregelmäßig, unbearbeitet, 1-3 cm stark</span></div><div class="num">45,00 €/m²</div><div class="num">53,55 €/m²</div></div>
  <div class="row col-w b" style="top:705px;height:23px"><div><span><b>Platten</b> wie vor, jedoch 4-7 cm stark</span></div><div class="num">50,00 €/m²</div><div class="num">59,50 €/m²</div></div>
  <div class="row col-w a" style="top:736px;height:23px"><div><span><b>Mauerabdeckplatten</b>, einseitig bearb. ansonsten unregelmäßig, 4-7 cm stark</span></div><div class="num">55,00 €/lfm</div><div class="num">59,50 €/lfm</div></div>

  <div class="tbl-head col-z" style="top:784px"><div>Zubehör</div><div class="n">Netto ab Werk</div><div class="n">Brutto ab Werk</div></div>
  <div class="row col-z a" style="top:826px;height:41px"><div class="top">Grauwacke-Riemchen, Einbindetiefe 2 cm,<br>Schichthöhe 4-19 cm</div><div class="num">160,00 €/m²</div><div class="num">190,40 €/m²</div></div>
  <div class="row col-z b" style="top:874px;height:23px"><div>Basaltlava-Abdeckplatten, bis 4 cm stark</div><div class="num">220,00 €/m²</div><div class="num">261,80 €/m²</div></div>

  <div class="tbl-head col-z" style="top:924px"><div>Logistik und Verpackung</div><div class="n">Netto ab Werk</div><div class="n">Brutto ab Werk</div></div>
  <div class="row col-z a" style="top:966px;height:23px"><div>Schüttgüter in Big-Bags (keine Gutschrift bei Rückgabe)</div><div class="num">30,00 €/St</div><div class="num">35,70 €/St</div></div>
  <div class="row col-z a" style="top:996px;height:40px"><div class="top">Wertsteine in Holz-Einweg-Kisten<br>(keine Gutschrift bei Rückgabe)</div><div class="num">40,00 €/St</div><div class="num">47,60 €/St</div></div>
  <div class="row col-z a" style="top:1043px;height:56px"><div class="top">Verladung von Rollschicht, Ecksteinen u. Bogensteinen in<br>Stahl-Mehrwegplatten (Rückgabepflicht)<br>Gutschrift bei frachtfreier Rückgabe</div><div class="num">50,00 €/St<br>45,00 €/St</div><div class="num">59,50 €/St<br>53,55 €/St</div></div>

  <div class="photo" role="img" aria-label="Foto Kräuterschnecke aus Grauwacke mit Kräutern" style="top:784px;height:131px;background:linear-gradient(180deg,#5d6650,var(--photo-4) 50%,#4f5a3c)"></div>
  <div class="caption" style="top:917px">Kräuterschnecke</div>
  <div class="photo" role="img" aria-label="Foto Findling zwischen Gräsern" style="top:948px;height:131px;background:linear-gradient(180deg,#8a8f6a,var(--photo-5) 45%,#5a4632)"></div>
  <div class="caption" style="top:1082px">Findling</div>

  <p class="fine">Die Preise verstehen sich ab Werk frei verladen, zuzüglich der gesetzlichen Mehrwertsteuer. Schüttgüter in größeren Mengen können aus laufender Produkton und aus Lagervorrat ständig geliefert werden. Für Lieferungen frei Baustelle mit Lastzügen oder Solofahrzeugen steht genügend Frachtraum zur Verfügung. Preise erhalten Sie auf Anfrage. Von Hand sortiert und bearbeitete Materialien bitten wir rechtzeitig zu bestellen. Durch den sehr hohen Lohnkostenanteil der Materialien ist der Verkauf nur gegen Barzahlung bei Abholung möglich. Sonderanfertigungen in Rollschicht, Bogensteinen, Ecksteinen usw. sind möglich.</p>

  <div class="foot-light"></div>
  <div class="foot-dark">www.tannhoferwerk.de</div>
</section>

</body>
</html>
```